High end business card design for custom homebuilding company

Looking for a high end business card design that is unique and elegant. Can use embossing, foil printing, laser die cutting, or any high end printing technique or high end paper. Will upload current design so you can see the logo and what we are using currently, but we want something more unique and elegant. I included our logo to help with design.

Target Market(s)

High end custom home buyers of $1.5 million plus homes. Also real estate developers of high end communities.

Industry/Entity Type

Business

Contact Information for Business Card

Double sided. We want something very elegant and expensive looking. We are looking to incorporate a combination of perhaps linen paper or a high end paper, with foil stamping or embossing/debossing to make the card look unique, but still elegant. We tend to use blacks and golds, but are open to any ideas. Looking for creative and unique design.

Colors

Designer to choose colors to be used in the design.

Requirements
Must have
• High end, elegant look. Can use foil, embossing, or high end papers like linen. We want to make the card unique and interesting, but elegant and expensive looking.
Nice to have
• I am including just some cards I saw that looked interesting for one reason or another. I like a clean elegant design and like both the clean white style, and the blacks. So not sure if we want a black design or white. Would like to see both.

```html
<!DOCTYPE html>
<html lang="en">
<head>
<meta charset="utf-8">
<title>Highcrest Homes – Business Card</title>
<link href="https://fonts.googleapis.com/css2?family=Exo+2:wght@400;500&display=swap" rel="stylesheet">
<style>
  :root {
    --ink: #000000;
    --slate: #141a19;
    --gold: #c9a866;
    --gold-light: #e6d3a0;
    --gold-deep: #9c7a3e;
    --steel: #5b6867;
  }
  html, body {
    margin: 0;
    padding: 0;
    overflow: hidden;
    background: var(--ink);
  }
  .card {
    position: relative;
    width: 1200px;
    height: 685px;
    overflow: hidden;
    background: var(--slate);
    font-family: "Exo 2", sans-serif;
  }
  .card__header {
    position: absolute;
    left: 0;
    top: 0;
    width: 1200px;
    height: 170px;
    background: var(--ink);
  }
  .card__band {
    position: absolute;
    left: 0;
    top: 170px;
    width: 1200px;
    height: 100px;
    background: linear-gradient(90deg, var(--gold-deep) 0%, var(--gold) 30%, #a8884f 55%, var(--steel) 85%, #3b4747 100%);
  }
  .brand {
    position: absolute;
    left: 88px;
    top: 62px;
    display: flex;
    align-items: center;
    gap: 16px;
  }
  .brand__mark {
    width: 22px;
    height: 22px;
    border-radius: 50%;
    background: var(--gold);
  }
  .brand__name {
    margin: 0;
    font-weight: 400;
    font-size: 44px;
    letter-spacing: 2px;
    color: var(--gold);
    line-height: 1;
  }
  .person {
    position: absolute;
    left: 110px;
    top: 430px;
  }
  .person__name {
    margin: 0;
    font-weight: 400;
    font-size: 52px;
    line-height: 1;
    letter-spacing: 1px;
    background: linear-gradient(90deg, var(--gold-deep), var(--gold-light) 55%, var(--gold));
    -webkit-background-clip: text;
    background-clip: text;
    color: transparent;
  }
  .person__title {
    margin: 10px 0 0 2px;
    font-weight: 400;
    font-size: 25px;
    letter-spacing: 8.5px;
    color: var(--gold);
    line-height: 1;
  }
  .contact {
    position: absolute;
    left: 746px;
    top: 338px;
    margin: 0;
    padding: 0;
    list-style: none;
    color: var(--gold);
    font-size: 22px;
    font-weight: 400;
    letter-spacing: 0.3px;
  }
  .contact__item {
    display: flex;
    align-items: center;
    min-height: 36px;
    margin-bottom: 15px;
  }
  .contact__item--address { margin-bottom: 18px; }
  .contact__icon {
    width: 34px;
    height: 34px;
    margin-right: 32px;
    flex: none;
  }
  .contact__icon--solid { fill: var(--gold); }
  .contact__icon--line {
    fill: none;
    stroke: var(--gold);
    stroke-width: 2;
  }
  .contact__text { line-height: 1.3; }
</style>
</head>
<body>
<div class="card">
  <div class="card__header"></div>
  <div class="card__band" role="img" aria-label="Gold and silver metallic ribbon band"></div>

  <div class="brand">
    <span class="brand__mark"></span>
    <h1 class="brand__name">HIGHCREST HOMES</h1>
  </div>

  <div class="person">
    <h2 class="person__name">MILES CARVER</h2>
    <p class="person__title">CREATIVE HEAD</p>
  </div>

  <ul class="contact">
    <li class="contact__item">
      <svg class="contact__icon contact__icon--solid" viewBox="0 0 24 24"><path d="M16 3 L21 6 L18 10 L15 8 C12 10 10 13 9 16 L11 18 L7 21 L4 18 C5 11 9 6 16 3 Z"/></svg>
      <span class="contact__text">(919) 555-0148</span>
    </li>
    <li class="contact__item">
      <svg class="contact__icon contact__icon--solid" viewBox="0 0 24 24"><text x="12" y="20" text-anchor="middle" font-family="Exo 2, sans-serif" font-size="28" font-weight="500">@</text></svg>
      <span class="contact__text">CARVER.MILES@EMAIL.COM</span>
    </li>
    <li class="contact__item contact__item--address">
      <svg class="contact__icon contact__icon--solid" viewBox="0 0 24 24"><path d="M12 3 L2 12 H5 V21 H10 V15 H14 V21 H19 V12 H22 Z"/></svg>
      <span class="contact__text">18 BIRCHWELL LN,<br>OAKVALE, NC, 27000</span>
    </li>
    <li class="contact__item">
      <svg class="contact__icon contact__icon--line" viewBox="0 0 24 24"><circle cx="12" cy="12" r="10"/><ellipse cx="12" cy="12" rx="4.5" ry="10"/><line x1="2" y1="12" x2="22" y2="12"/><line x1="12" y1="2" x2="12" y2="22"/><line x1="4" y1="7" x2="20" y2="7"/><line x1="4" y1="17" x2="20" y2="17"/></svg>
      <span class="contact__text">WWW.HIGHCRESTHOMES.COM</span>
    </li>
    <li class="contact__item">
      <svg class="contact__icon contact__icon--solid" viewBox="0 0 24 24"><rect x="2" y="2" width="20" height="20" rx="2"/></svg>
      <span class="contact__text">FOLLOWHIGHCREST</span>
    </li>
  </ul>
</div>
</body>
</html>
```